Startup company business card (Media & Advertising)

we need a business card design for a company that is a startup in the media and aggregation industry. Card needs to look funky and of a new breed/modern and upmarket.

Target Market(s)

advertisers/ brand agencies & media publishers

Industry/Entity Type

Advertising

Contact Information for Business Card

Please ensure the front face signifies our brand (plumvexo.com) and back has details for the contact. Standard contact such as phone , address, email , website etc.

Font styles to use
Other font styles liked:
• use styleguide and logo font and color

Colors

Designer to choose colors to be used in the design.

Requirements
Must have
• We are disrupting the media and agency industry so subtlety would be good to use imagery to signify this
Nice to have
• Please use logo colors for branding
Should not have
• be as creative and provide few options. Pick a brand color from logo and styleguide

```html
<!DOCTYPE html>
<html lang="en">
<head>
<meta charset="utf-8">
<title>plumvexo business card</title>
<link rel="stylesheet" href="https://fonts.googleapis.com/css2?family=Lato:wght@400;700;900&display=swap">
<style>
  :root {
    --stage: #2b2b2b;
    --paper: #ffffff;
    --ink: #2a2a2a;
    --ink-soft: #555555;
    --brand-red: #ea3a4e;
    --night: #262626;
    --night-deep: #1c1c1c;
    --night-light: #333333;
  }
  * { box-sizing: border-box; margin: 0; padding: 0; }
  html, body { width: 1200px; height: 900px; overflow: hidden; }
  body {
    background: var(--stage);
    font-family: "Lato", sans-serif;
    position: relative;
  }
  .card {
    position: absolute;
    left: 320px;
    width: 560px;
    height: 320px;
    border-radius: 3px;
    overflow: hidden;
    box-shadow: 0 10px 30px rgba(0,0,0,0.45);
  }

  /* Contact face */
  .card--contact { top: 100px; background: var(--paper); }
  .card--contact .brand {
    position: absolute; top: 34px; right: 36px;
    display: flex; align-items: center; gap: 12px;
  }
  .brand__dot { width: 26px; height: 26px; border-radius: 50%; background: var(--brand-red); }
  .brand__name { font-weight: 900; font-size: 30px; color: var(--ink); letter-spacing: 0.5px; }
  .person { position: absolute; top: 120px; left: 40px; }
  .person__name { color: var(--brand-red); font-weight: 700; font-size: 19px; }
  .person__role { color: var(--ink-soft); font-size: 12px; margin-top: 2px; }
  .contacts { position: absolute; left: 40px; bottom: 42px; list-style: none; }
  .contacts li {
    display: flex; align-items: center; gap: 12px;
    font-size: 13px; color: var(--ink-soft); line-height: 20px;
  }
  .contacts svg { width: 13px; height: 13px; fill: var(--brand-red); flex: none; }
  .contacts .address { color: var(--brand-red); font-weight: 700; line-height: 17px; margin-top: 4px; padding-left: 25px; }
  .card--contact .band {
    position: absolute; left: 0; right: 0; bottom: 0; height: 9px; background: var(--brand-red);
  }

  /* Brand face */
  .card--brand { top: 480px; background: var(--night); }
  .card--brand .texture {
    position: absolute; inset: 0;
    background: linear-gradient(135deg, var(--night-light) 0%, var(--night) 45%, var(--night-deep) 100%);
  }
  .card--brand .brand {
    position: absolute; top: 100px; left: 0; right: 0;
    display: flex; justify-content: center; align-items: center; gap: 18px;
  }
  .card--brand .brand__dot { width: 58px; height: 58px; }
  .card--brand .brand__name { color: var(--paper); font-size: 54px; }
  .tagline {
    position: absolute; top: 222px; left: 0; right: 0; text-align: center;
    color: var(--brand-red); font-weight: 700; font-size: 14px; letter-spacing: 0.8px;
  }
  .website {
    position: absolute; top: 246px; left: 0; right: 0; text-align: center;
    color: var(--paper); font-weight: 700; font-size: 13px;
  }
</style>
</head>
<body>
  <section class="card card--contact">
    <div class="brand">
      <span class="brand__dot"></span>
      <span class="brand__name">plumvexo</span>
    </div>
    <div class="person">
      <p class="person__name">Maren Tollis</p>
      <p class="person__role">Law Attorney</p>
    </div>
    <ul class="contacts">
      <li>
        <svg viewBox="0 0 16 16" aria-hidden="true"><path d="M3 1l3 3-2 2c1 2 3 4 5 5l2-2 3 3-2 3C6 15 1 10 1 3z"/></svg>
        (416) 555 0148
      </li>
      <li>
        <svg viewBox="0 0 16 16" aria-hidden="true"><path d="M4 1h8v4H4zM1 6h14v6h-3v3H4v-3H1zM5 10v4h6v-4z"/></svg>
        (416) 555 0193
      </li>
      <li>
        <svg viewBox="0 0 16 16" aria-hidden="true"><path d="M1 3h14v10H1zM2 4l6 5 6-5v1L8 10 2 5z" fill-rule="evenodd"/></svg>
        maren@plumvexo.com
      </li>
      <li class="address">45 Alder Street W., Suite 310<br>Toronto ON, M4X 1K7</li>
    </ul>
    <div class="band"></div>
  </section>

  <section class="card card--brand">
    <div class="texture" role="img" aria-label="Faint dark low-poly geometric texture"></div>
    <div class="brand">
      <span class="brand__dot"></span>
      <span class="brand__name">plumvexo</span>
    </div>
    <p class="tagline">REACH EVERY SCREEN, EVERY DAY!</p>
    <p class="website">www.plumvexo.com</p>
  </section>
</body>
</html>
```